Baby Adoption Announcement

I'm looking for a simple, understated and modern baby adoption announcement.

The baby is a boy, but I don't want anything that is blue or particularly boyish. No storks, baby baskets, rattles, or traditional baby announcement designs. No cutesy or busy designs.

Should measure 5.25 x 8.25 inches to fit in an A9 envelope.

Simple graphics MIGHT include birds, grasses, trees, rivers. I'm open to other ideas. Text can be a single color or multi colored. Graphics are not mandatory.

Since this is text heavy, I'd like the designer to be REALLY GOOD at choosing fonts and typesetting.

Text should read:

Memory answers us bright on your face—
Impossibly, we spoke and were silent
Together before all of this. (in italics)

Tavorin Corvalen Tesky Marvo
Born on March 16, 2012 in Boston, MA
and entrusted to us by his birthmother, Quelda.

Named Tavorin, which means God is with us, after Quelda’s grandfather &
Corvalen, after Corv and St. Corvalen of Dursa

• Should measure 5.25 x 8.25 inches to fit in A9 envelope.

• The baby is a boy, but I don't want anything that is blue or particularly boyish. No storks, baby baskets, rattles, or traditional baby announcement designs. Nothing cutesy or busy.

```html
<!DOCTYPE html>
<html lang="en">
<head>
<meta charset="utf-8">
<title>Adoption Announcement</title>
<link rel="stylesheet" href="https://fonts.googleapis.com/css2?family=Didact+Gothic&family=Reenie+Beanie&display=swap">
<style>
  :root {
    --page: #ffffff;
    --ink: #0a86a8;
    --sky-pale: #e6f4fc;
    --sky-mid: #bfe6f8;
    --sky-deep: #27c2f2;
    --sun: #fbf6c4;
    --grass: #a9dcf5;
  }
  * { margin: 0; padding: 0; box-sizing: border-box; }
  html, body {
    width: 1200px; height: 826px; overflow: hidden;
    background: var(--page);
  }
  .card {
    position: absolute;
    left: 347px; top: 15px;
    width: 506px; height: 796px;
    overflow: hidden;
    color: var(--ink);
    font-family: "Didact Gothic", "Century Gothic", sans-serif;
    text-align: center;
  }
  .sky-art {
    position: absolute; inset: 0;
    background:
      radial-gradient(circle at 18% 14%, var(--sun) 0, rgba(251,246,196,0.6) 12%, rgba(251,246,196,0) 28%),
      radial-gradient(ellipse at 75% 10%, rgba(255,255,255,0.85) 0, rgba(255,255,255,0) 22%),
      linear-gradient(200deg, var(--sky-deep) 0%, var(--sky-mid) 30%, var(--sky-pale) 65%, var(--sky-pale) 100%);
  }
  .grass-art {
    position: absolute; left: 0; right: 0; bottom: 0; height: 110px;
    background: linear-gradient(to bottom, rgba(169,220,245,0) 0%, var(--grass) 100%);
  }
  .block { position: absolute; left: 0; right: 0; }
  .verse { top: 112px; font-size: 25px; line-height: 42px; letter-spacing: -0.3px; }
  .verse .closing {
    font-family: "Reenie Beanie", cursive;
    font-size: 44px; line-height: 40px; display: block; margin-top: 2px;
  }
  .name { top: 312px; font-size: 50px; line-height: 62px; letter-spacing: -0.5px; }
  .name .initial { font-family: "Reenie Beanie", cursive; font-size: 64px; }
  .birth { top: 468px; font-size: 25px; line-height: 35px; letter-spacing: -0.3px; }
  .naming { top: 610px; font-size: 19px; line-height: 29px; letter-spacing: -0.4px; }
</style>
</head>
<body>
  <main class="card">
    <div class="sky-art" role="img" aria-label="Soft sky illustration with a pale sun, clouds and flowing swirls"></div>
    <div class="grass-art" role="img" aria-label="Pale blue grass silhouettes along the bottom edge"></div>

    <p class="block verse">
      Memory answers us bright on your face -<br>
      Impossibly, we spoke &amp; were silent
      <span class="closing">Together before all of this.</span>
    </p>

    <h1 class="block name" style="font-weight:400">
      <span class="initial">T</span>avorin <span class="initial">C</span>orvalen<br>
      <span class="initial">T</span>esky <span class="initial">M</span>arvo
    </h1>

    <p class="block birth">
      Born on March 16, 2012 in Boston, MA<br>
      &amp; entrusted to us<br>
      by his birthmother, Quelda.
    </p>

    <p class="block naming">
      Named Tavorin, which means God is with us,<br>
      after Quelda’s grandfather &amp; Corvalen, after Corv<br>
      &amp; St. Corvalen of Dursa
    </p>
  </main>
</body>
</html>
```